Brookvale Brochure & Fact Sheet

We need a brochure designed that we will distribute both digitally (PDF) and also have printed. We our an IT company and would like the creative to reflect our brand and industry. All content is written and ready to go. We need each page of the brochure provided as an individual file so we can arrange the pages as needed.

```html
<!DOCTYPE html>
<html lang="en">
<head>
<meta charset="utf-8">
<title>Brookvale Fact Sheet</title>
<link href="https://fonts.googleapis.com/css2?family=Carlito:wght@400;700&display=swap" rel="stylesheet">
<style>
  :root{
    --page-bg:#e9e6e1;
    --sheet:#ffffff;
    --ink:#2b2b2b;
    --ink-strong:#1e1e1e;
    --brand-blue:#1b62ad;
    --band-dark:#161616;
    --band-light:#ececec;
    --band-mid:#cfcfcf;
    --photo-deep:#1b1746;
    --photo-violet:#5b3aa8;
    --photo-blue:#2f6fd0;
  }
  *{margin:0;padding:0;box-sizing:border-box}
  html,body{width:1200px;height:1200px;overflow:hidden}
  body{background:var(--page-bg);font-family:"Carlito","Calibri",sans-serif;color:var(--ink)}
  .sheet{position:absolute;left:150px;top:18px;width:900px;height:1164px;background:var(--sheet);box-shadow:0 4px 18px rgba(0,0,0,.18)}
  .masthead{position:absolute;left:0;top:0;width:900px;height:85px}
  .masthead svg{position:absolute;inset:0}
  .masthead-title{position:absolute;left:40px;top:22px;font-size:38px;font-weight:400;color:var(--ink-strong);letter-spacing:.5px}
  .brand{position:absolute;right:42px;top:20px;display:flex;align-items:center;gap:10px}
  .brand-dot{width:30px;height:30px;border-radius:50%;background:#fff}
  .brand-name{font-size:40px;font-weight:700;color:#fff;letter-spacing:-1px;line-height:1}
  .column{position:absolute;top:135px;width:399px;font-size:14.6px;line-height:19.9px;text-align:justify}
  .column-left{left:41px}
  .column-right{left:460px}
  .lead{color:var(--brand-blue);font-weight:700}
  .approach-title{font-size:20px;font-weight:700;color:var(--ink-strong);margin:18px 0 20px;text-align:left}
  .service-title{font-weight:700;color:var(--ink-strong);text-align:left}
  .service{margin-bottom:20px}
  .photo{position:absolute;left:41px;top:803px;width:818px;height:278px;background:linear-gradient(180deg,var(--photo-deep) 0%,var(--photo-violet) 45%,var(--photo-blue) 70%,#2a2348 100%)}
  .footer{position:absolute;left:0;top:1100px;width:900px;height:64px;background:var(--band-dark);display:flex;align-items:center;justify-content:center;font-size:17px;color:var(--brand-blue)}
  .footer b{font-weight:700}
  .footer .sep{margin:0 10px;color:var(--brand-blue)}
</style>
</head>
<body>
<div class="sheet">
  <header class="masthead">
    <svg width="900" height="85" viewBox="0 0 900 85">
      <rect width="900" height="85" fill="var(--band-dark)"/>
      <polygon points="0,0 332,0 284,85 0,85" fill="var(--band-light)"/>
      <polygon points="310,0 332,0 284,85 270,85" fill="var(--band-mid)"/>
    </svg>
    <div class="masthead-title">FACT SHEET</div>
    <div class="brand"><span class="brand-dot"></span><span class="brand-name">brookvale</span></div>
  </header>

  <div class="column column-left">
    <p class="lead">Managed Services by Brookvale delivers proactive monitoring, maintenance, security and IT support for small and medium size business infrastructures, applications and cloud solutions. Based in West Michigan, we provide a hands-on service approach and design end-to-end IT solutions that help your company grow efficiently, remain flexible, and maintain a lean IT operation. We employ a dedicated team of infrastructure experts that ensure your business operations are running smoothly, with no downtime, 24 hours a day. IT shouldn't be a disruption, but a reliable tool, and it's our job to make that happen.</p>
    <h2 class="approach-title">Our Managed IT Services Approach</h2>
    <div class="service">
      <h3 class="service-title">Infrastructure</h3>
      <p>We specialize in first architecting a streamlined IT system that works harmoniously and increases workflow efficiency. We then manage, monitor, and maintain all business networks and servers either on your premise or remotely. We provide 24-hour advanced network monitoring to all Managed Services partners; this allows us to proactively respond to alerts, avoid downtime, identify bottlenecks and manage security vulnerabilities. When it comes to IT, we stay on top of things – so you don't have to.</p>
    </div>
    <div class="service">
      <h3 class="service-title">Security</h3>
      <p>Our security services include endpoint security, network security, cloud security and policy management. We focus on protecting our partners from today's sophisticated cyber security threats by helping them outline, implement and maintain customized security policies and procedures. We stay abreast of all security developments and threats and</p>
    </div>
  </div>

  <div class="column column-right">
    <p class="service">strive to educate everyone on how to protect themselves both personally and professionally.</p>
    <div class="service">
      <h3 class="service-title">Disaster Recovery</h3>
      <p>No matter how well protected you are, it's better to plan for the unexpected. Brookvale collaborates with partners to plan, provide and manage disaster recovery solutions specific to their IT needs. Our disaster recovery plan includes off-site backups, complex disaster recovery solutions, and redundancy solutions. Be proactive and get your plan B in order with Brookvale.</p>
    </div>
    <div class="service">
      <h3 class="service-title">Desktop Management</h3>
      <p>We help your employees focus on the day-to-day business at hand by setting up efficient workstations, consistently keeping systems up-to-date, and fielding support questions 24/7. Count on reliable and secured workspaces from Brookvale.</p>
    </div>
    <div class="service">
      <h3 class="service-title">Cloud Management</h3>
      <p>Valuable business data needs to be stored and protected. We help businesses determine the best model for their needs, whether it's in the cloud, hosted on-site, or a hybrid of the two, and assist them with implementation, monitoring and maintenance.</p>
    </div>
    <div class="service">
      <h3 class="service-title">Customer service is at the core of our Brookvale team.</h3>
      <p>Our Managed IT Services is successful because we have a dedicated and experienced team ensuring your staff receives rapid responses and expert support from technicians they know and trust.</p>
    </div>
  </div>

  <div class="photo" role="img" aria-label="Wide photo of a large technology conference hall with an audience facing lit stage screens under purple and blue lighting"></div>

  <footer class="footer">
    <span>Phone <b>1.866.555.0142</b></span><span class="sep">|</span>
    <span>Email <b>info@brookvale.com</b></span><span class="sep">|</span>
    <span><b>www.brookvale.com</b></span>
  </footer>
</div>
</body>
</html>
```